plumbing & gas fitting business card design

We need a business card design for a plumbing & gas fitting company. The company covers commercial, domestic and maintenance work. We would like a modern design communicating efficiency and sophistication. preferred colours would include (red grey & black) or (green grey & black). Please DO NOT include any water droplets.

Industry/Entity Type

Business

Contact Information for Business Card

Vortig Plumbing & Gas, Commercial Domestic & Maintenance, licence no. 617394K, ABN 47215830962, Phone 0417382956, Email vortigplumbingandgas@corvanet.com

```html
<!DOCTYPE html>
<html lang="en">
<head>
<meta charset="utf-8">
<title>Vortig Plumbing &amp; Gas — Business Card</title>
<link rel="stylesheet" href="https://fonts.googleapis.com/css2?family=Roboto+Condensed:wght@700&family=Roboto:wght@400&display=swap">
<style>
  :root {
    --green: #8dc63f;
    --black: #000000;
    --white: #ffffff;
    --backdrop: #f2f2f2;
    --backdrop-edge: #dcdcdc;
  }
  * { margin: 0; padding: 0; box-sizing: border-box; }
  html, body { width: 1200px; height: 1000px; overflow: hidden; }
  body {
    position: relative;
    background: radial-gradient(ellipse at 50% 40%, var(--backdrop) 0%, var(--backdrop) 45%, var(--backdrop-edge) 100%);
    font-family: "Roboto", Arial, sans-serif;
  }
  .brand-name {
    font-family: "Roboto Condensed", "Arial Narrow", sans-serif;
    font-weight: 700;
    white-space: nowrap;
  }

  /* standalone brand lockup */
  .brand-lockup {
    position: absolute;
    left: 740px; top: 115px; width: 390px;
    display: flex; flex-direction: column; align-items: center;
  }
  .brand-lockup .brand-square {
    width: 190px; height: 190px; background: var(--green);
  }
  .brand-lockup .brand-name {
    margin-top: 38px; font-size: 34px; color: var(--green);
  }

  /* card front */
  .card { position: absolute; overflow: hidden; }
  .card-front {
    left: 60px; top: 250px; width: 640px; height: 370px;
    background: var(--green);
    box-shadow: 0 4px 10px rgba(0,0,0,0.25);
    display: flex; flex-direction: column; align-items: center; justify-content: center;
  }
  .card-front .brand-square { width: 165px; height: 165px; background: var(--black); }
  .card-front .brand-name { margin-top: 22px; font-size: 27px; color: var(--black); }

  /* card back */
  .card-back {
    left: 452px; top: 590px; width: 606px; height: 350px;
    background: var(--black);
    box-shadow: 0 4px 10px rgba(0,0,0,0.3);
  }
  .card-back .back-brand {
    position: absolute; left: 50px; top: 55px; width: 175px;
    display: flex; flex-direction: column; align-items: center;
  }
  .card-back .brand-square { width: 85px; height: 85px; background: var(--green); }
  .card-back .brand-name { margin-top: 18px; font-size: 15px; color: var(--green); }

  .contact-list {
    position: absolute; left: 272px; top: 188px;
    list-style: none; color: var(--white); font-size: 15px;
  }
  .contact-list li { display: flex; align-items: center; gap: 8px; height: 24px; }
  .contact-icon { width: 20px; height: 14px; fill: var(--green); }

  .card-footer {
    position: absolute; left: 0; bottom: 0; width: 100%; height: 72px;
    background: var(--green);
    text-align: center; font-size: 10px; color: #1a1a1a; padding-top: 16px;
  }
</style>
</head>
<body>

  <div class="brand-lockup">
    <div class="brand-square"></div>
    <div class="brand-name">Vortig Plumbing &amp; Gas</div>
  </div>

  <section class="card card-front">
    <div class="brand-square"></div>
    <div class="brand-name">Vortig Plumbing &amp; Gas</div>
  </section>

  <section class="card card-back">
    <div class="back-brand">
      <div class="brand-square"></div>
      <div class="brand-name">Vortig Plumbing &amp; Gas</div>
    </div>

    <ul class="contact-list">
      <li>
        <svg class="contact-icon" viewBox="0 0 20 14" aria-hidden="true">
          <path d="M1 5 Q10 -1 19 5 L17 7 L14 5.5 L14 4 Q10 2.5 6 4 L6 5.5 L3 7 Z"/>
          <rect x="4" y="7" width="12" height="6" rx="1.5"/>
        </svg>
        <span>0417382956</span>
      </li>
      <li>
        <svg class="contact-icon" viewBox="0 0 20 14" aria-hidden="true">
          <rect x="1" y="1" width="18" height="12"/>
          <path d="M1 1 L10 8 L19 1" fill="none" stroke="#000" stroke-width="1.4"/>
        </svg>
        <span>vortigplumbingandgas@corvanet.com</span>
      </li>
    </ul>

    <footer class="card-footer">Commercial Domestic &amp; Maintenance, licence no. 617394K, ABN 47215830962,</footer>
  </section>

</body>
</html>
```